Vorlisk.com Redesign

Please read the notes and see the site-map attached.
Updates

We are looking for something highly creative. Please provide your best work. Best of luck and thank you very much for your hard work!

Project Deadline Extended
Reason: I am seeing good designs but I am not seeing great designs. I really need a design that is unique and is going to wow me. No one is required to stick to the existing color schemes etc. You are free to use other colors etc. I am seeing a lot of the same colors that are used on the site now.

Target Market(s)

Business and entrepreneurs mainly. People looking to build applications, software or launch web or mobile tech products.

Colors

Designer to choose colors to be used in the design.

Requirements
Must have
• See my attached html file.
Nice to have
Should not have
• No sure

```html
<!DOCTYPE html>
<html lang="en">
<head>
<meta charset="utf-8">
<title>Vorlisk.com</title>
<link href="https://fonts.googleapis.com/css2?family=Open+Sans:wght@300;400;600&family=Arimo:ital,wght@0,400;1,400&display=swap" rel="stylesheet">
<style>
:root{
  --navy:#2b4a5f;
  --footer:#2a4456;
  --footer-dark:#223a4a;
  --login:#2f5168;
  --text:#666a6e;
  --line:#d9dcde;
  --icon:#8a8f93;
  --white:#ffffff;
  --orange:#f59a2b;
}
*{margin:0;padding:0;box-sizing:border-box}
html,body{width:754px;height:1200px;overflow:hidden;background:#fff}
body{position:relative;font-family:"Arimo",Arial,sans-serif;color:var(--text)}
.abs{position:absolute}
.caps{font-family:"Open Sans",sans-serif;text-transform:uppercase;letter-spacing:.12em}

/* hero */
.hero{position:absolute;left:0;top:0;width:754px;height:367px;
  background:radial-gradient(ellipse at 70% 55%,#5a3a3a 0%,#3a3030 35%,#22262b 75%,#1a1d21 100%)}
.brand{left:110px;top:20px;display:flex;align-items:center;gap:8px;color:var(--white);
  font-family:"Open Sans",sans-serif;font-weight:600;font-size:19px}
.brand .mark{width:24px;height:24px;border-radius:50%;border:2px solid var(--white)}
.nav{left:306px;top:40px;display:flex;gap:22px;font-size:7px;color:var(--white)}
.login{left:586px;top:35px;width:54px;height:17px;background:var(--login);color:var(--white);
  font-size:6.5px;display:flex;align-items:center;justify-content:center;letter-spacing:.08em}
.hero h1{left:107px;top:122px;font-family:"Open Sans",sans-serif;font-weight:300;font-size:38px;color:var(--white)}
.lede{left:110px;top:176px;width:300px;font-family:"Open Sans",sans-serif;font-weight:300;font-size:14px;line-height:19.5px;color:#eee}
.more{left:108px;top:251px;width:176px;height:28px;border:1px solid var(--white);color:var(--white);
  font-size:8px;display:flex;align-items:center;justify-content:center}
.device{left:420px;top:85px;width:150px;height:282px;border-radius:30px 30px 0 0;
  background:linear-gradient(180deg,#e8e8e8 0%,#c9a78f 60%,#a07a62 100%);opacity:.9}

/* section headings */
.title{width:754px;text-align:center;font-size:13px;color:var(--navy);letter-spacing:.14em}
.intro{left:137px;width:480px;text-align:center;font-size:6.5px;line-height:13.5px}

/* services */
.svc{display:flex;align-items:center;gap:13px}
.ring{width:45px;height:45px;border-radius:50%;border:1px solid #c8cbcd;display:flex;align-items:center;justify-content:center}
.svc-label{font-size:7px;line-height:12.5px;color:var(--navy);letter-spacing:.1em}
.rule{left:0;top:550px;width:754px;height:1px;background:var(--line)}

/* fit */
.fit-title{left:205px;top:591px;font-size:12.5px;color:var(--navy);letter-spacing:.14em}
.portrait{left:253px;top:621px;width:120px;height:120px;border-radius:50%;
  background:radial-gradient(circle at 55% 45%,#e9d8c6 0%,#d8c2b0 40%,#b49bb8 100%)}
.select{left:151px;top:755px;width:224px;height:22px;border:1px solid #cfd2d4;font-size:6.5px;
  display:flex;align-items:center;justify-content:space-between;padding:0 8px 0 10px;color:#555}
.fit-copy{left:140px;top:789px;width:235px;text-align:right;font-size:6.5px;line-height:13.5px}
.need{left:425px;width:230px;display:flex;align-items:center;gap:12px}
.need .ring{width:37px;height:37px;flex:none}
.need p{font-size:6.5px;line-height:13.5px}
.chev{color:#b9bdc0;font-size:14px;font-family:"Open Sans",sans-serif;font-weight:300}

/* testimonials */
.quote{display:flex;gap:19px;align-items:flex-start}
.avatar{width:70px;height:70px;border-radius:50%;flex:none}
.quote h3{font-size:7.5px;color:var(--navy);letter-spacing:.12em;font-weight:400;margin-top:6px}
.quote .date{font-style:italic;font-size:6px;margin-top:4px}
.quote p{font-size:6.5px;line-height:13.5px;margin-top:5px;width:160px}

/* footer */
.footer{left:0;top:1071px;width:754px;height:101px;background:var(--footer)}
.footer-bar{left:0;top:1172px;width:754px;height:28px;background:var(--footer-dark);
  text-align:center;font-size:6px;color:#c9d2d8;padding-top:9px}
.fcol{color:#d2dbe1;font-size:5.8px;line-height:13.5px}
.fcol h4{font-family:"Open Sans",sans-serif;font-weight:400;font-size:7.5px;letter-spacing:.14em;color:var(--white);margin-bottom:7px}
.social{display:flex;align-items:center;gap:4px;margin-bottom:6px}
.social span.dot{width:18px;height:18px;border-radius:50%;border:1px solid #9fb0bc}
.chat{left:660px;top:1150px;width:86px;height:29px;background:var(--orange);color:var(--white);
  font-family:"Open Sans",sans-serif;font-weight:600;font-size:10px;display:flex;align-items:center;justify-content:center}
</style>
</head>
<body>

<header class="hero">
  <div class="abs brand"><span class="mark"></span>vorlisk</div>
  <nav class="abs nav caps"><span>Home</span><span>About Us</span><span>Our Work</span><span>Services</span><span>Reach Us</span></nav>
  <div class="abs login caps">Login »</div>
  <h1 class="abs">Vorlisk</h1>
  <p class="abs lede">We create web and mobile products that delight users, create smiles and deliver more than expected.</p>
  <div class="abs more caps">Click here for more info &nbsp;»</div>
  <div class="abs device" role="img" aria-label="Hand holding a smartphone showing the brand splash screen"></div>
  <svg class="abs" style="left:58px;top:172px" width="12" height="44"><path d="M11 1 L1 22 L11 43" fill="none" stroke="#9aa0a6" stroke-width="1"/></svg>
  <svg class="abs" style="left:688px;top:172px" width="12" height="44"><path d="M1 1 L11 22 L1 43" fill="none" stroke="#9aa0a6" stroke-width="1"/></svg>
</header>

<h2 class="abs title caps" style="top:390px;font-weight:400">Services</h2>
<p class="abs intro" style="top:422px">We offer a full range of web development services for anyone looking to create a bold statement. We create elegant websites that captivate the vision of our clients. We specialize in the development of rich internet applications that make a splash and are super easy to use.</p>

<div class="abs svc" style="left:109px;top:477px">
  <div class="ring"><svg width="22" height="16"><rect x="3" y="1" width="16" height="11" fill="none" stroke="var(--icon)"/><path d="M0 14 H22" stroke="var(--icon)" stroke-width="2"/></svg></div>
  <div class="svc-label caps">Web<br>Development</div>
</div>
<div class="abs svc" style="left:238px;top:477px">
  <div class="ring"><svg width="12" height="20"><rect x="1" y="1" width="10" height="18" rx="2" fill="none" stroke="var(--icon)"/><circle cx="6" cy="16" r="1" fill="var(--icon)"/></svg></div>
  <div class="svc-label caps">Mobile App<br>Development</div>
</div>
<div class="abs svc" style="left:373px;top:477px">
  <div class="ring"><svg width="24" height="22"><ellipse cx="10" cy="4" rx="8" ry="3" fill="var(--icon)"/><rect x="2" y="4" width="16" height="12" fill="var(--icon)"/><circle cx="18" cy="16" r="5" fill="#fff" stroke="var(--icon)"/></svg></div>
  <div class="svc-label caps">Custom Software<br>Development</div>
</div>
<div class="abs svc" style="left:524px;top:477px">
  <div class="ring"><svg width="16" height="20"><path d="M5 1 V11 H3 V14 L7 19 H14 V11 H8 V1 Z" fill="var(--icon)"/></svg></div>
  <div class="svc-label caps">User Experience<br>Design</div>
</div>

<div class="abs rule"></div>

<h2 class="abs fit-title caps" style="font-weight:400">Whatever you can fit</h2>
<div class="abs portrait" role="img" aria-label="Portrait photo of a smiling client wearing glasses"></div>
<div class="abs select"><span>Web Development</span><svg width="9" height="6"><path d="M1 1 L4.5 5 L8 1" fill="none" stroke="#888"/></svg></div>
<p class="abs fit-copy">We offer a full range of web development services for anyone looking to create a bold statement. We create elegant websites that captivate the vision of our clients. We specialize in the development of rich internet applications that make a splash and are super easy to use.</p>

<div class="abs need" style="top:590px"><div class="ring"><svg width="12" height="14"><path d="M2 13 L6 2 L11 8 Z" fill="var(--icon)"/></svg></div><p>My existing website really needs a new look and a technology upgrade as well.</p></div>
<div class="abs need" style="top:646px"><div class="ring"><svg width="16" height="14"><rect x="1" y="6" width="3" height="7" fill="none" stroke="var(--icon)"/><path d="M5 6 L8 1 L9 5 H14 L13 13 H5 Z" fill="none" stroke="var(--icon)"/></svg></div><p>I need a shiny new website. Can you help me create an amazing web presence?</p></div>
<div class="abs need" style="top:697px"><div class="ring"><svg width="16" height="14"><rect x="3" y="3" width="10" height="8" fill="none" stroke="var(--icon)"/><path d="M1 1h3M12 1h3M1 13h3M12 13h3" stroke="var(--icon)"/></svg></div><p>We need to expand our presence in the mobile world and need a mobile website that looks amazing and works well on all types of mobile devices.</p></div>
<div class="abs need" style="top:753px"><div class="ring"><svg width="14" height="16"><circle cx="7" cy="5" r="4" fill="var(--icon)"/><path d="M0 16 Q7 7 14 16 Z" fill="var(--icon)"/></svg></div><p>I am a designer or agency and already have an amazing design for my website\application. I need a development quote.</p></div>
<div class="abs need" style="top:808px"><div class="ring"><svg width="22" height="14"><rect x="1" y="2" width="11" height="8" fill="none" stroke="var(--icon)"/><path d="M0 12h13" stroke="var(--icon)"/><rect x="15" y="1" width="5" height="4" fill="none" stroke="var(--icon)"/><rect x="15" y="8" width="5" height="4" fill="none" stroke="var(--icon)"/></svg></div><p>I need to create a rich internet application or web product and need to get a quote.</p></div>

<span class="abs chev" style="left:74px;top:720px">〈</span>
<span class="abs chev" style="left:664px;top:720px">〉</span>

<h2 class="abs title caps" style="top:891px;font-weight:400">Testimonials</h2>
<p class="abs intro" style="top:920px">We offer a full range of web development services for anyone looking to create a bold statement. We create elegant websites that captivate the vision of our clients. We specialize in the development of rich internet applications that make a splash and are super easy to use.</p>

<div class="abs quote" style="left:125px;top:970px">
  <div class="avatar" role="img" aria-label="Photo of a client in a suit" style="background:radial-gradient(circle at 50% 40%,#9aa3ab,#3d4650)"></div>
  <div><h3 class="caps">Marlon Teague</h3><div class="date">Posted on 27 march 2014</div><p>It is a long established fact that a reader will be distracted by the readable content...</p></div>
</div>
<div class="abs quote" style="left:394px;top:970px">
  <div class="avatar" role="img" aria-label="Photo of a smiling client" style="background:radial-gradient(circle at 50% 40%,#e8d6c4,#7a8a9a)"></div>
  <div><h3 class="caps">Marlon Teague</h3><div class="date">Posted on 27 march 2014</div><p>It is a long established fact that a reader will be distracted by the readable content...</p></div>
</div>
<span class="abs chev" style="left:95px;top:1000px">〈</span>
<span class="abs chev" style="left:646px;top:1000px">〉</span>

<footer class="abs footer"></footer>
<div class="abs fcol" style="left:114px;top:1087px"><h4>ABOUT US</h4>Who We Are<br>Our Process</div>
<div class="abs fcol" style="left:211px;top:1087px"><h4>SERVICES</h4>Web Development<br>Mobile App Development<br>Custom Software Development<br>User Experience Design</div>
<div class="abs fcol" style="left:340px;top:1087px"><h4>CONTACT</h4>Vorlisk LLC<br>2280 Harlow Ave #310<br>Brenford, CA 90517</div>
<div class="abs fcol" style="left:443px;top:1101px">Voice: +1 (555) 014-2290<br>Email: reachus@vorlisk.com<br>Chat ID: vorlisk</div>
<div class="abs fcol" style="left:556px;top:1087px"><h4>SOCIAL</h4>
  <div class="social"><span class="dot"></span>: Friendlink</div>
  <div class="social"><span class="dot"></span>: Chirper</div>
</div>
<div class="abs footer-bar">© 2014 Vorlisk LLC. Privacy Policy</div>
<div class="abs chat">Live Chat</div>

</body>
</html>
```